Business Card Design

The business card is for an IT services company with a specialism
in Integration Services Markets are Health, Government and finance, we provide Velmora SOA platforms and CWR Trellis integration. We are developing multi-agency connectivity

Industry/Entity Type

Business

Contact Information for Business Card

Martin Gorse
Director

BQVo Ltd Martin.gorse@bqvoltd.co.uk

Mobile: +44 (0) 7700900418
Tel: +44 (0) 1632 960583
Website: www.bqvoltd.co.uk

Fenwright House, Fenwright Square, Harrowby ZX98 4QT

Percival Hanley
Health Integration Services

Mobile +44 (0) 07700900276
Tel +44 (0) 1632 960583
Address as above

```html
<!DOCTYPE html>
<html lang="en">
<head>
<meta charset="utf-8">
<title>BQVo Ltd – Business Card</title>
<link rel="stylesheet" href="https://fonts.googleapis.com/css2?family=Pathway+Gothic+One&display=swap">
<style>
  :root {
    --card-white: #ffffff;
    --ink: #4a5357;
    --green: #45b549;
    --green-mid: #6fc36c;
    --green-pale: #a6d9a2;
  }
  html, body {
    margin: 0;
    padding: 0;
    width: 1200px;
    height: 791px;
    overflow: hidden;
    background: var(--card-white);
  }
  .card {
    position: relative;
    width: 1200px;
    height: 791px;
    background: var(--card-white);
    font-family: "Pathway Gothic One", "Arial Narrow", sans-serif;
    color: var(--ink);
  }
  .side-band {
    position: absolute;
    left: 0;
    top: 0;
    width: 167px;
    height: 791px;
    background: linear-gradient(180deg, var(--green) 0%, var(--green-mid) 100%);
  }
  .hex-cluster {
    position: absolute;
    left: 0;
    top: 0;
    width: 1200px;
    height: 791px;
  }
  .person-name {
    position: absolute;
    left: 203px;
    top: 80px;
    margin: 0;
    font-size: 68px;
    font-weight: 400;
    line-height: 1;
    letter-spacing: 0.5px;
  }
  .person-role {
    position: absolute;
    left: 203px;
    top: 150px;
    margin: 0;
    font-size: 40px;
    line-height: 1;
  }
  .company-name {
    position: absolute;
    right: 193px;
    top: 128px;
    margin: 0;
    font-size: 118px;
    font-weight: 400;
    line-height: 1;
    white-space: nowrap;
  }
  .company-web {
    position: absolute;
    right: 193px;
    top: 250px;
    margin: 0;
    font-size: 40px;
    line-height: 1;
  }
  .contact-list {
    position: absolute;
    left: 203px;
    top: 540px;
    margin: 0;
    padding: 0;
    list-style: none;
    font-size: 47px;
    line-height: 46px;
  }
  .contact-address {
    position: absolute;
    left: 203px;
    top: 692px;
    margin: 0;
    font-size: 47px;
    line-height: 1;
    font-style: normal;
    white-space: nowrap;
  }
</style>
</head>
<body>
  <div class="card">
    <div class="side-band" role="img" aria-label="Green honeycomb pattern band"></div>

    <svg class="hex-cluster" viewBox="0 0 1200 791" role="img" aria-label="Cluster of green honeycomb hexagons">
      <defs>
        <linearGradient id="cluster-fill" x1="0" y1="0" x2="1" y2="1">
          <stop offset="0" stop-color="#45b549"/>
          <stop offset="0.5" stop-color="#7cc878"/>
          <stop offset="1" stop-color="#45b549"/>
        </linearGradient>
      </defs>
      <polygon fill="url(#cluster-fill)"
        points="1075,121 1200,121 1200,700 1172,751 1075,751 1020,660 880,575 790,490 718,420 718,340 770,305 1030,305 1030,215 1060,215"/>
    </svg>

    <h1 class="person-name">MARTIN GORSE</h1>
    <p class="person-role">Director</p>

    <h2 class="company-name">BQVo Ltd</h2>
    <p class="company-web">www.bqvoltd.co.uk</p>

    <ul class="contact-list">
      <li>Mobile: +44 (0) 7700900418</li>
      <li>Tel: +44 (0) 1632 960583</li>
      <li>Email: Martin.gorse@bqvoltd.co.uk</li>
    </ul>
    <address class="contact-address">Fenwright House, Fenwright Square, Harrowby ZX98 4QT</address>
  </div>
</body>
</html>
```